Lantern Stew Poster and Social Media Art

We need a recognisable poster/social media brand that can be updated for each quarterly event. Each Lantern Stew event has many of the same elements, (inclusive for all people, including gay, bi, straight, queer, old, young, lesbian and everything inbetween), at the same funky cool venue (The Corvane), hosted by Harriet Quill and her gang of Drag Kings and Queens and music supplied by two cracking DJ's, - Pale Falcon and Side Step. Lantern Stew is a regular (quarterly) event in southeast Queensland, Australia, that welcomes all colours of the rainbow and every kind of person, including people who don't think this kind of event is for them. Get out of the house, bring your smile and get your fancy tickled by irrepressible host and Drag Queen extraordinaire, Harriet Quill and their delightfully diverse gathering of goodtime-gangsta DJ's for song, dance and giggly games at The Corvnae in Nambour.
Have provided three 'soup' concept art files - and the four messy disappointing files used to date. of the posters produced this far - the stronges of them is the 'Harbour Night'

```html
<!DOCTYPE html>
<html lang="en">
<head>
<meta charset="utf-8">
<title>Lantern Stew – Harbour Night</title>
<link rel="stylesheet" href="https://fonts.googleapis.com/css2?family=Cinzel:wght@700&family=Anton&display=swap">
<style>
:root{
  --night:#1a0508;
  --maroon:#4a0d12;
  --red:#a3121c;
  --red-deep:#6e0a10;
  --gold:#e8c474;
  --gold-light:#fff1c4;
  --gold-dark:#9c6a22;
  --ink:#0b0b0b;
  --white:#ffffff;
}
*{margin:0;padding:0;box-sizing:border-box}
html,body{width:849px;height:1200px;overflow:hidden;background:var(--night)}
.poster{position:relative;width:849px;height:1200px;overflow:hidden;
  background:radial-gradient(circle at 20% 10%,#5a1a1c 0%,var(--maroon) 30%,var(--night) 75%)}
.backdrop{position:absolute;inset:0;
  background:
    linear-gradient(160deg,transparent 0 38%,rgba(255,170,40,.35) 48%,transparent 62%),
    radial-gradient(ellipse at 50% 35%,rgba(190,40,30,.55),transparent 60%),
    radial-gradient(ellipse at 50% 90%,rgba(230,120,40,.35),transparent 55%)}
.band{position:absolute;inset:0}
.event-name{position:absolute;left:0;right:0;top:112px;text-align:center;
  font-family:"Cinzel",serif;font-weight:700;color:var(--gold);line-height:1}
.event-name .line-one{display:block;font-size:96px}
.event-name .line-two{display:block;font-size:104px;margin-top:14px}
.edition{position:absolute;left:0;right:0;top:346px;text-align:center;
  font-family:"Cinzel",serif;font-weight:700;font-size:38px;color:var(--gold)}
.can-photo{position:absolute;left:240px;top:410px;width:330px;height:560px;border-radius:40px 40px 60px 60px;
  background:linear-gradient(180deg,#c0202a 0%,#8e0e14 30%,#eeeeee 31%,#d8d8d8 78%,#c8a28a 86%,#b98a70 100%)}
.hosts{position:absolute;left:62px;top:470px;transform:rotate(-10deg);transform-origin:left top;
  font-family:"Anton",sans-serif;color:var(--white);line-height:.95;
  text-shadow:-2px -2px 0 var(--ink),2px -2px 0 var(--ink),-2px 2px 0 var(--ink),2px 2px 0 var(--ink),5px 5px 0 var(--ink)}
.hosts .label{font-size:24px;letter-spacing:1px;padding-left:6px}
.hosts .name{font-size:52px;letter-spacing:2px}
.hosts .indent{padding-left:34px}
.hosts .indent-more{padding-left:60px}
.hosts .and{font-size:22px;vertical-align:middle;margin-right:8px}
.features{position:absolute;right:59px;top:448px;text-align:right;font-family:"Anton",sans-serif;
  color:var(--gold);font-size:39px;line-height:49.5px;letter-spacing:2px}
.dj-disc{position:absolute;left:80px;top:740px;width:234px;height:234px;border-radius:50%;
  background:radial-gradient(circle,#2a2a2a 0 60%,#111 72%,#6b2a10 74%,#3a1206 100%)}
.djs{position:absolute;left:40px;top:785px;width:310px;text-align:center;font-family:"Anton",sans-serif;
  color:var(--white);line-height:1;
  text-shadow:-2px -2px 0 var(--ink),2px -2px 0 var(--ink),-2px 2px 0 var(--ink),2px 2px 0 var(--ink)}
.djs .label{font-size:24px;letter-spacing:1px}
.djs .name{font-size:42px;letter-spacing:2px;margin-top:6px}
.djs .and{font-size:20px}
.price-burst{position:absolute;left:540px;top:695px;width:240px;height:240px}
.price{position:absolute;font-family:"Anton",sans-serif;color:var(--white);line-height:1;
  text-shadow:-2px -2px 0 var(--ink),2px -2px 0 var(--ink),-2px 2px 0 var(--ink),2px 2px 0 var(--ink),4px 4px 0 var(--ink)}
.price .tier{display:block;font-size:16px;letter-spacing:.5px}
.price .amount{display:block;font-size:58px}
.price-eb{left:582px;top:722px}
.price-eb .tier{padding-left:26px}
.price-ga{left:688px;top:772px}
.price-door{left:592px;top:832px}
.red-band{position:absolute;left:0;top:1086px;width:849px;height:38px;
  background:linear-gradient(90deg,var(--red-deep),#e0161e 50%,var(--red-deep))}
.date-board{position:absolute;left:107px;top:984px;width:646px;height:116px;border-radius:24px;
  background:var(--red);border:3px solid var(--gold)}
.date-board-inner{position:absolute;left:22px;right:22px;top:18px;bottom:18px;border-radius:16px;
  background:var(--ink);border:2px solid var(--gold-dark);display:flex;align-items:center;justify-content:center;
  font-family:"Cinzel",serif;font-weight:700;font-size:50px}
.date-text{background:linear-gradient(180deg,var(--gold-light),var(--gold) 50%,var(--gold-dark));
  -webkit-background-clip:text;background-clip:text;color:transparent;white-space:nowrap}
.date-text sup{font-size:24px;vertical-align:top;margin-right:22px}
.gold-band{position:absolute;left:0;top:1124px;width:849px;height:76px;
  background:linear-gradient(90deg,#b98a3e,var(--gold-light) 50%,#b98a3e);
  display:flex;align-items:center;justify-content:center;font-family:"Anton",sans-serif;
  font-size:40px;letter-spacing:2px;color:var(--ink)}
</style>
</head>
<body>
<main class="poster">
  <div class="backdrop" role="img" aria-label="Glowing stage lights and star shapes in red and amber behind the event name"></div>

  <svg class="band" width="849" height="1200" viewBox="0 0 849 1200" aria-hidden="true">
    <polygon points="0,570 849,406 849,790 0,965" fill="#000"/>
  </svg>

  <div class="can-photo" role="img" aria-label="Hand holding a red and white soup can printed with the event name and date"></div>

  <h1 class="event-name"><span class="line-one">LANTERN</span><span class="line-two">STEW</span></h1>
  <div class="edition">HARBOUR NIGHT</div>

  <div class="hosts">
    <div class="label">HOSTED BY</div>
    <div class="name">RORY</div>
    <div class="name indent">VANTAGE</div>
    <div class="name indent"><span class="and">AND</span>HARRIET</div>
    <div class="name indent-more">QUILL</div>
  </div>

  <div class="features">
    <div>DRAG</div><div>SHOWS</div><div>COMEDY</div><div>DANCING</div><div>PRIZES</div>
  </div>

  <div class="dj-disc"></div>
  <div class="djs">
    <div class="label">BEATS BY DJS</div>
    <div class="name">PALE FALCON</div>
    <div class="and">and</div>
    <div class="name">SIDE STEP</div>
  </div>

  <svg class="price-burst" viewBox="0 0 240 240" aria-hidden="true">
    <defs><linearGradient id="burstGold" x1="0" y1="0" x2="1" y2="1"><stop offset="0" stop-color="#fff1c4"/><stop offset=".5" stop-color="#e8c474"/><stop offset="1" stop-color="#9c6a22"/></linearGradient></defs>
    <polygon fill="url(#burstGold)" points="120,0 142,40 185,18 182,66 232,70 200,108 240,140 194,154 212,200 166,190 150,236 120,202 90,236 74,190 28,200 46,154 0,140 40,108 8,70 58,66 55,18 98,40"/>
  </svg>
  <div class="price price-eb"><span class="tier">EB</span><span class="amount">$15</span></div>
  <div class="price price-ga"><span class="tier">GA ONLINE</span><span class="amount">$20</span></div>
  <div class="price price-door"><span class="tier">AT THE DOOR</span><span class="amount">$25</span></div>

  <div class="red-band"></div>
  <div class="date-board">
    <div class="date-board-inner"><span class="date-text">FRIDAY SEPT 26<sup>TH</sup>7:00</span></div>
  </div>

  <div class="gold-band">PRIZES FOR BEST CARNIVAL ATTIRE!</div>
</main>
</body>
</html>
```